Financial Markets Algorithmic Trading solution needs One pager Marketing designs

We are creating Marketing sheets that will be handed to potential clients that will give a broad base of our products available. We are an established Sell side firm in the financial Industry and our product focus is a Technology base solution and we want to showcases our Algorithmic trading suite.
Our customer base is Buy-side Traders,hedge funds, managing directors. We want a clean high end technology based look that will encompass the colors that are in our logo.
We intend to work with the designer after initial design to encompass the theme to other pages we have. So we will need a design that can be part of a set but can stand alone.

** i have uploaded a new File that is the correct File to design to. Please follow the flow of the categories and what resides under those headers. This is key for the delivery of the material****

Target Market(s)

Finance- Buy side firms, geared for meetings and info sheets to be left with clients who are CEO's , Head Traders, Managing Directors

Industry/Entity Type

Financial Service

Font styles to use
Other font styles liked:
• Tw Cen MT

Requirements
Must have
• Must include the logo, and encompass the colors that are in the logo.
• We want this to have a Technology company feel to it. We would like it clean and unique, all while not falling into the normal classic business look.
• Also for this page we would like to keep the layout similar to what we have.
• Please keep the style of lettering
Should not have
• Messy look, overpowering color. no cartoon graphics

```html
<!DOCTYPE html>
<html lang="en">
<head>
<meta charset="utf-8">
<title>Algorithmic Trading Strategy Overview</title>
<link rel="stylesheet" href="https://fonts.googleapis.com/css2?family=Jost:wght@300;400;500;600;700&display=swap">
<style>
  :root {
    --navy: #14213d;
    --ink: #3a3f4a;
    --orange: #f7941d;
    --blue: #0a7cc4;
    --panel: #eef0f7;
    --rule: #6b6f7a;
    --backdrop: #d6d6d8;
  }
  * { margin: 0; padding: 0; box-sizing: border-box; }
  html, body { width: 960px; height: 1200px; overflow: hidden; background: var(--backdrop); }
  body { position: relative; font-family: "Jost", sans-serif; }

  .sheet {
    position: absolute; left: 57px; top: 0;
    width: 790px; height: 1120px;
    transform: scale(1.0714); transform-origin: 0 0;
    overflow: hidden;
    background: linear-gradient(180deg, var(--panel) 0%, #f3f4fa 60%, #e8ecf6 100%);
  }
  .shapes { position: absolute; inset: 0; }

  .title {
    position: absolute; left: 86px; top: 54px;
    font-size: 20px; font-weight: 600; letter-spacing: 0.6px;
    color: #fff; white-space: nowrap;
  }
  .title .accent { color: var(--orange); }

  .intro {
    position: absolute; left: 0; top: 108px;
    font-size: 11.5px; font-weight: 600; letter-spacing: 0.4px;
    color: var(--navy); line-height: 18px;
  }
  .intro span {
    display: block; white-space: nowrap;
    text-align: justify; text-align-last: justify;
  }
  .intro .last { text-align-last: left; }
  .intro .firm { font-size: 15px; font-weight: 700; letter-spacing: 0.4px; }

  .brand {
    position: absolute; left: 520px; top: 219px;
    display: flex; align-items: center; gap: 10px;
  }
  .brand-dot { width: 48px; height: 48px; border-radius: 50%; background: var(--orange); }
  .brand-name { font-size: 20px; font-weight: 500; color: var(--blue); letter-spacing: 0.2px; white-space: nowrap; }

  .category {
    position: absolute; left: 50px;
    border-left: 1px solid var(--rule); border-top: 1px solid var(--rule);
  }
  .category-label {
    position: absolute; left: -26px; bottom: 0;
    writing-mode: vertical-rl; transform: rotate(180deg);
    font-size: 14px; font-weight: 600; letter-spacing: 0.4px; white-space: nowrap;
  }
  .label-orange { color: var(--orange); }
  .label-blue { color: var(--blue); }

  .strategy { padding-left: 10px; margin-bottom: 14px; }
  .strategy:first-of-type { padding-top: 8px; }
  .strategy h3 {
    font-size: 11px; line-height: 14px; font-weight: 600; letter-spacing: 0.8px;
    color: var(--navy); margin-bottom: 1px; white-space: nowrap;
  }
  .strategy p {
    font-size: 9.4px; font-weight: 400; color: var(--ink);
    line-height: 14.5px; letter-spacing: 0.15px; white-space: nowrap;
  }
</style>
</head>
<body>
<main class="sheet">
  <svg class="shapes" viewBox="0 0 790 1120" width="790" height="1120">
    <defs>
      <linearGradient id="topBand" x1="0" y1="0" x2="1" y2="0.4">
        <stop offset="0" stop-color="#b9bccb"/>
        <stop offset="0.55" stop-color="#a8b6ca"/>
        <stop offset="1" stop-color="#b7d6ea"/>
      </linearGradient>
      <linearGradient id="skyField" x1="0" y1="0" x2="0" y2="1">
        <stop offset="0" stop-color="#bfdcef"/>
        <stop offset="1" stop-color="#e2eef8"/>
      </linearGradient>
      <linearGradient id="orangeFade" x1="0" y1="0" x2="0" y2="1">
        <stop offset="0" stop-color="#f7941d"/>
        <stop offset="0.7" stop-color="#f7941d"/>
        <stop offset="1" stop-color="#fcd3a0"/>
      </linearGradient>
      <radialGradient id="portraitTone" cx="0.55" cy="0.4" r="0.7">
        <stop offset="0" stop-color="#3e8f8b"/>
        <stop offset="0.55" stop-color="#1b4a4b"/>
        <stop offset="1" stop-color="#0c2224"/>
      </radialGradient>
    </defs>

    <rect x="0" y="0" width="790" height="410" fill="url(#topBand)"/>
    <polygon points="365,1120 790,690 790,1120" fill="url(#skyField)"/>
    <polygon points="620,540 790,370 790,690 700,780" fill="#c9e1f2"/>
    <polygon points="525,165 790,165 790,352 520,330 452,245" fill="#f4f6f9"/>
    <polygon points="365,800 425,740 425,860" fill="#cfe3f3"/>

    <polygon points="78,23 78,160 93,150 93,33" fill="#ffffff"/>
    <polygon points="27,95 93,45 93,160" fill="var(--orange)"/>

    <polygon points="290,410 425,280 425,545" fill="var(--blue)"/>
    <polygon points="425,350 675,600 425,850" fill="url(#orangeFade)"/>

    <path d="M395,1120 L400,880 C410,760 480,700 585,700 C690,700 765,770 765,880 L765,1120 Z"
          fill="url(#portraitTone)" role="img"
          aria-label="Photograph: profile of a human head with turning gears inside, in dark teal tones"/>
  </svg>

  <h1 class="title"><span class="accent">Alg</span>orithmic Trading Strategy Overview</h1>

  <div class="intro">
    <span style="margin-left:98px;width:447px"><b class="firm">Castell &amp; Partners</b> has partnered with an award winning</span>
    <span style="margin-left:98px;width:427px">algorithmic trading platform and developed a custom suite of</span>
    <span style="margin-left:98px;width:412px">algorithms designed to ensure high quality execution. Our</span>
    <span style="margin-left:45px;width:445px">algorithms incorporate our unique ATX point of sale order types</span>
    <span style="margin-left:45px;width:425px">(pQuote* / rQuote*) seamlessly into each strategy. This</span>
    <span style="margin-left:45px;width:407px">integration smooth's workflow, improves execution quality,</span>
    <span style="margin-left:45px;width:390px">ensures greater liquidity sourcing, minimizes information</span>
    <span style="margin-left:45px;width:370px">leakage and brings a wide variety of Algo and SOR</span>
    <span style="margin-left:45px;width:353px">strategies directly into your OMS, EMS, or proprietary</span>
    <span style="margin-left:45px;width:353px">trading platform. In addition, we work in a</span>
    <span style="margin-left:45px;width:335px">consultative role to develop custom DMA routes,</span>
    <span style="margin-left:45px;width:317px">design algorithms according to client needs or</span>
    <span style="margin-left:45px;width:280px">specific requirements, &amp; implement unique</span>
    <span style="margin-left:45px;width:265px">routing strategies designed to efficiently</span>
    <span style="margin-left:45px;width:242px">touch today's complex market</span>
    <span class="last" style="margin-left:45px;width:242px">micro-strategy.</span>
  </div>

  <div class="brand">
    <div class="brand-dot"></div>
    <div class="brand-name">castell&amp;partners</div>
  </div>

  <section class="category" style="top:423px;width:245px;height:180px">
    <div class="category-label label-orange">Liquidity Sourcing</div>
    <div class="strategy">
      <h3>“SOR”</h3>
      <p>Optimizes order placement in lit and dark venues<br>to maximize liquidity capture and minimize information<br>leakage. The strategy balances “Urgency to capture the<br>display quote” vs. opportunities to seek out dark liquidity to<br>minimize information leakage and price improvement.</p>
    </div>
    <div class="strategy">
      <h3>DARK AGG</h3>
      <p>Manages order placement in dark venues to optimize liquidity capture<br>and reduce information leakage. The strategy attempts to first discover<br>liquidity by slicing optimally sized orders at various venues, and then<br>rebalances intelligently to venues where it has detected liquidity.</p>
    </div>
  </section>

  <section class="category" style="top:655px;width:368px;height:155px">
    <div class="category-label label-blue">Schedule Driven</div>
    <div class="strategy">
      <h3>“VWAP”</h3>
      <p>Trades using historical volume profile to target VWAP as the benchmark.<br>The strategy can optionally accept StartTime and EndTime as parameters<br>to schedule trading in a given trading period. The strategy utilizes<br>passive and aggressive trading tactics to achieve liquidity.</p>
    </div>
    <div class="strategy">
      <h3>“TWAP”</h3>
      <p>Similar to the VWAP strategy with a different schedule.<br>The schedule is a constant rate of trading between the given<br>StartTime and EndTime.</p>
    </div>
  </section>

  <section class="category" style="top:863px;width:355px;height:152px">
    <div class="category-label label-orange">Dynamic &amp; Adaptive</div>
    <div class="strategy">
      <h3>“POV”</h3>
      <p>Tracks volume from the time the order starts trading and trades<br>according to the specified target participation percentage.<br>Continuous optimizations are made as the order trades to<br>target optima price and liquidity goals.</p>
    </div>
    <div class="strategy">
      <h3>“ARRIVAL PRICE”</h3>
      <p>Manages the trade-off between market<br>impact and volatility (price risk) to<br>optimally execute the order.</p>
    </div>
  </section>
</main>
</body>
</html>
```